Need a corporate background Image with our existing logo for Zoom or Microsoft Teams

Hi,

We require a corporate background image with our existing logo use with Zoom or Microsoft Teams.

Our existing logo is at https://www.halvenrock-systems.com/images/logo_top.png

Thank you.

```html
<!DOCTYPE html>
<html lang="en">
<head>
<meta charset="utf-8">
<title>Halvenrock Systems – Meeting Backgrounds</title>
<link rel="stylesheet" href="https://fonts.googleapis.com/css2?family=Archivo:wght@800&display=swap">
<style>
  :root {
    --board: #c4c4c4;
    --white: #ffffff;
    --brand-blue: #1466ad;
    --sky: #7fb5dd;
    --line-grey: #848488;
  }
  html, body {
    margin: 0;
    width: 1038px;
    height: 1200px;
    overflow: hidden;
    background: var(--board);
  }
  .board {
    position: relative;
    width: 1038px;
    height: 1200px;
  }
  .banner {
    position: absolute;
    left: 116px;
    width: 807px;
    height: 453px;
    background: var(--white);
    box-shadow: 0 2px 10px rgba(0, 0, 0, 0.35);
  }
  .banner--plain { top: 113px; }
  .banner--portrait { top: 633px; }
  .banner svg { display: block; width: 100%; height: 100%; }
  .defs { position: absolute; width: 0; height: 0; }

  .panel-blue { fill: url(#blueField); }
  .panel-white { fill: var(--white); }
  .frame-line { fill: none; stroke: var(--line-grey); stroke-width: 9; stroke-linejoin: miter; }
  .slash { stroke: var(--line-grey); stroke-width: 9; }
  .hex-mist { fill: url(#mistFill); }
  .hex-glass { fill: url(#glassFill); stroke: rgba(127, 181, 221, 0.45); stroke-width: 2; }
  .hex-sky { fill: var(--sky); }
  .panel-steel { fill: url(#steelField); }
  .brand-mark { fill: var(--brand-blue); }
  .brand-name {
    fill: var(--brand-blue);
    font-family: 'Archivo', Arial, sans-serif;
    font-weight: 800;
  }
  .brand-name--main { font-size: 58px; }
  .brand-name--sub { font-size: 26px; }
  .portrait-area { fill: url(#portraitFill); }
</style>
</head>
<body>
<svg class="defs" aria-hidden="true">
  <defs>
    <linearGradient id="blueField" x1="0" y1="0" x2="1" y2="1">
      <stop offset="0" stop-color="#1593dc"/>
      <stop offset="1" stop-color="#0470bd"/>
    </linearGradient>
    <linearGradient id="steelField" x1="0" y1="0" x2="1" y2="1">
      <stop offset="0" stop-color="#7a7a7f"/>
      <stop offset="1" stop-color="#919196"/>
    </linearGradient>
    <radialGradient id="mistFill" cx="0.5" cy="0.5" r="0.6">
      <stop offset="0" stop-color="#ffffff"/>
      <stop offset="1" stop-color="#e6e6e6"/>
    </radialGradient>
    <radialGradient id="glassFill" cx="0.5" cy="0.5" r="0.6">
      <stop offset="0" stop-color="rgba(255,255,255,0.2)"/>
      <stop offset="1" stop-color="rgba(160,200,235,0.55)"/>
    </radialGradient>
    <linearGradient id="portraitFill" x1="0" y1="0" x2="0" y2="1">
      <stop offset="0" stop-color="#d9d9db"/>
      <stop offset="0.45" stop-color="#7a7a7e"/>
      <stop offset="1" stop-color="#4a4a4d"/>
    </linearGradient>
  </defs>
</svg>

<div class="board">
  <section class="banner banner--plain">
    <svg viewBox="0 0 1393 783" aria-label="Halvenrock Systems meeting background">
      <polygon class="panel-blue" points="0,0 388,0 173,393 388,783 0,783"/>
      <polygon class="panel-white" points="0,105 305,105 463,393 305,680 0,680"/>
      <polyline class="frame-line" points="0,123 293,123 448,393 293,663 0,663"/>
      <polygon class="panel-blue" points="0,141 283,141 296,165 173,393 296,622 283,645 0,645"/>
      <line class="slash" x1="455" y1="0" x2="348" y2="188"/>
      <line class="slash" x1="327" y1="220" x2="267" y2="330"/>
      <polygon class="hex-mist" points="453,160 722,160 855,393 722,624 453,624 319,393"/>
      <polygon class="hex-glass" points="597,689 677,543 847,543 930,689 847,835 677,835"/>
      <polygon class="hex-sky" points="1108,354 1190,354 1208,390 1165,390 1108,488 1070,421"/>
      <polygon class="hex-sky" points="1023,419 1032,404 1049,404 1057,419 1049,434 1032,434"/>
      <polygon class="hex-sky" points="1021,481 1037,453 1069,453 1085,481 1069,509 1037,509"/>
      <polygon class="panel-steel" points="1165,390 1393,390 1393,783 1118,783 1028,627"/>
      <circle class="brand-mark" cx="903" cy="122" r="44"/>
      <text class="brand-name brand-name--main" x="985" y="148" textLength="345" lengthAdjust="spacingAndGlyphs">HALVENROCK</text>
      <text class="brand-name brand-name--sub" x="988" y="182" textLength="340" lengthAdjust="spacing">SYSTEMS</text>
    </svg>
  </section>

  <section class="banner banner--portrait">
    <svg viewBox="0 0 1393 783" aria-label="Halvenrock Systems meeting background with portrait">
      <polygon class="panel-blue" points="0,0 388,0 173,393 388,783 0,783"/>
      <polygon class="panel-white" points="0,105 305,105 463,393 305,680 0,680"/>
      <polyline class="frame-line" points="0,123 293,123 448,393 293,663 0,663"/>
      <polygon class="panel-blue" points="0,141 283,141 296,165 173,393 296,622 283,645 0,645"/>
      <line class="slash" x1="455" y1="0" x2="348" y2="188"/>
      <line class="slash" x1="327" y1="220" x2="267" y2="330"/>
      <polygon class="hex-mist" points="453,160 722,160 855,393 722,624 453,624 319,393"/>
      <rect class="portrait-area" x="425" y="165" width="545" height="618" rx="12"
            role="img" aria-label="Photo of a businessman in a grey suit seated in a black leather armchair"/>
      <polygon class="hex-sky" points="1108,354 1190,354 1208,390 1165,390 1108,488 1070,421"/>
      <polygon class="hex-sky" points="1023,419 1032,404 1049,404 1057,419 1049,434 1032,434"/>
      <polygon class="hex-sky" points="1021,481 1037,453 1069,453 1085,481 1069,509 1037,509"/>
      <polygon class="panel-steel" points="1165,390 1393,390 1393,783 1118,783 1028,627"/>
      <circle class="brand-mark" cx="903" cy="122" r="44"/>
      <text class="brand-name brand-name--main" x="985" y="148" textLength="345" lengthAdjust="spacingAndGlyphs">HALVENROCK</text>
      <text class="brand-name brand-name--sub" x="988" y="182" textLength="340" lengthAdjust="spacing">SYSTEMS</text>
    </svg>
  </section>
</div>
</body>
</html>
```